Bref créative
Brochure for Professional Services Firm
Brightfen Partners
We need a great design for a brochure to be used as marketing collateral at tradeshows and for general marketing purposes. Our website is brightfenpartners.example to get additional information. We generally work with oilfield service companies.
Consulting
Corporate, professional.
===========Update==========
Requirement : Trifold
Our logo files.
Here is a sample presentation we currently use to market our services.
Some stock photos we have.
stock photos.
stock photo.

```html
<!DOCTYPE html>
<html lang="en">
<head>
<meta charset="utf-8">
<title>Brightfen Partners – Trifold Brochure</title>
<link rel="stylesheet" href="https://fonts.googleapis.com/css2?family=Roboto+Condensed:ital,wght@0,400;0,700;1,700&family=Lora:ital@1&display=swap">
<style>
  :root {
    --cyan: #1aa3d6;
    --cyan-light: #6cc7ea;
    --navy: #1b2a3a;
    --ink: #4a4f55;
    --paper: #ffffff;
    --backdrop: #e4e5e6;
    --steel: #8a98a6;
    --sky: #9fc3dc;
  }
  * { margin: 0; padding: 0; box-sizing: border-box; }
  html, body { width: 1200px; height: 799px; overflow: hidden; background: var(--backdrop); }
  body { position: relative; font-family: "Roboto Condensed", sans-serif; color: var(--ink); }

  .sheet { position: absolute; background: var(--paper); box-shadow: 0 4px 14px rgba(0,0,0,.12); }
  .sheet-inside { left: 50px; top: 40px; width: 560px; height: 720px; }
  .sheet-outside { left: 650px; top: 230px; width: 500px; height: 330px; }

  .panel { position: absolute; left: 0; width: 100%; height: 240px; border-bottom: 1px dashed #d5dadf; }
  .panel:last-child { border-bottom: none; }
  .panel-top { top: 0; } .panel-mid { top: 240px; } .panel-bottom { top: 480px; }

  .photo { position: absolute; }
  .photo-gears { left: 300px; top: 14px; width: 240px; height: 92px; background: linear-gradient(135deg, #c9d0d6, #7d8892); }
  .photo-pylons { left: 20px; top: 96px; width: 190px; height: 130px; background: linear-gradient(180deg, #5f86ab, #2c3f55); }
  .photo-pumpjack { left: 300px; top: 14px; width: 240px; height: 110px; background: linear-gradient(180deg, var(--sky) 0%, #c8dbe8 55%, #8c8a5c 56%, #6d7048 100%); }
  .photo-plant { left: 20px; top: 150px; width: 240px; height: 80px; background: linear-gradient(135deg, #6c7680, #2e353c); }
  .photo-lines { left: 20px; top: 14px; width: 240px; height: 120px; background: linear-gradient(180deg, #7ea9d3, #33577c); }
  .photo-executive { right: 16px; top: 70px; width: 200px; height: 230px; background: linear-gradient(160deg, #c3d7e6, #4d6b86 70%, #26364a); }

  .chevrons { display: inline-block; vertical-align: middle; margin-right: 6px; }

  .section-title { position: absolute; left: 20px; top: 18px; font-weight: 700; font-size: 30px; color: var(--cyan); text-transform: uppercase; letter-spacing: .5px; }
  .tagline { position: absolute; left: 22px; top: 58px; width: 250px; font-family: "Lora", serif; font-style: italic; font-size: 10px; line-height: 1.4; color: var(--ink); }

  .service { position: absolute; }
  .service-heading { font-family: "Lora", serif; font-style: italic; font-size: 14px; color: var(--navy); padding-bottom: 4px; border-bottom: 2px solid var(--cyan); margin-bottom: 8px; }
  .service p { font-family: "Lora", serif; font-style: italic; font-size: 10px; line-height: 1.5; color: var(--ink); margin-bottom: 6px; }
  .service-transaction { left: 230px; top: 112px; width: 310px; }
  .service-financial { left: 20px; top: 14px; width: 260px; }
  .service-cfo { left: 280px; top: 14px; width: 260px; }
  .service-cfo ul { list-style: none; font-size: 11px; line-height: 1.7; color: var(--ink); }
  .service-cfo li::before { content: "› "; color: var(--cyan); font-weight: 700; }

  .pull-quote { position: absolute; left: 280px; top: 140px; width: 260px; font-family: "Lora", serif; font-style: italic; font-size: 12px; line-height: 1.5; color: var(--cyan); text-align: center; }

  .caption-box { position: absolute; left: 20px; top: 144px; width: 240px; padding: 10px 12px; border-left: 4px solid var(--cyan); background: #eef7fb; font-size: 11px; line-height: 1.4; color: var(--navy); }

  .frame-rule { position: absolute; background: var(--cyan); }
  .rule-left { left: 0; top: 0; width: 6px; height: 100%; }
  .rule-bottom { left: 0; bottom: 0; width: 100%; height: 6px; }

  .brand { position: absolute; left: 130px; top: 26px; display: flex; align-items: center; gap: 8px; }
  .brand-mark { width: 14px; height: 14px; background: var(--navy); }
  .brand-name { font-weight: 700; font-size: 18px; letter-spacing: 1.5px; color: var(--navy); text-transform: uppercase; }

  .headline { position: absolute; left: 28px; top: 120px; font-weight: 700; font-style: italic; text-transform: uppercase; line-height: 1.05; }
  .headline .line { display: block; }
  .headline .big { font-size: 40px; color: var(--navy); }
  .headline .small { font-size: 22px; color: var(--cyan); }
  .headline-bar { position: absolute; left: 28px; top: 104px; width: 90px; height: 4px; background: var(--cyan); }
</style>
</head>
<body>

<section class="sheet sheet-inside" aria-label="Brochure inside spread">
  <div class="panel panel-top">
    <h2 class="section-title">
      <svg class="chevrons" width="28" height="22" viewBox="0 0 28 22"><path d="M0 0h8l7 11-7 11H0l7-11z M12 0h8l7 11-7 11h-8l7-11z" fill="#1aa3d6"/></svg>Services
    </h2>
    <p class="tagline">Brightfen financial and transaction advisory services for small and mid sized companies</p>
    <div class="photo photo-gears" role="img" aria-label="Close-up photo of steel gears and bearings"></div>
    <div class="photo photo-pylons" role="img" aria-label="Photo of electrical transmission towers against a blue sky"></div>
    <div class="service service-transaction">
      <h3 class="service-heading"><svg class="chevrons" width="16" height="12" viewBox="0 0 28 22"><path d="M0 0h8l7 11-7 11H0l7-11z M12 0h8l7 11-7 11h-8l7-11z" fill="#1aa3d6"/></svg>Transaction Advisory Services</h3>
      <p>We have worked through several transactions and know what it takes to get a deal closed. We also know how much executive management can get sidetracked in managing the demands of the transaction. Brightfen will work with you and your team to make sure the right story gets told to buyers and the process stays on track.</p>
    </div>
  </div>

  <div class="panel panel-mid">
    <div class="service service-financial">
      <h3 class="service-heading"><svg class="chevrons" width="16" height="12" viewBox="0 0 28 22"><path d="M0 0h8l7 11-7 11H0l7-11z M12 0h8l7 11-7 11h-8l7-11z" fill="#1aa3d6"/></svg>Financial Advisory Services</h3>
      <p>From budgeting and forecasting to cash flow planning, our advisors give owners a clear view of the numbers that drive their business and the decisions ahead.</p>
      <p>We build practical reporting tools so your team can act on accurate information every month.</p>
    </div>
    <div class="photo photo-pumpjack" role="img" aria-label="Photo of an oilfield pumpjack on open grassland"></div>
    <div class="photo photo-plant" role="img" aria-label="Photo of industrial oilfield equipment"></div>
    <p class="pull-quote">We will work with you to plan for growth, manage your cash and build the value of your business.</p>
  </div>

  <div class="panel panel-bottom">
    <div class="photo photo-lines" role="img" aria-label="Photo of power lines and towers at dusk"></div>
    <p class="caption-box">Experienced advisors serving oilfield service companies across the region.</p>
    <div class="service service-cfo">
      <h3 class="service-heading"><svg class="chevrons" width="16" height="12" viewBox="0 0 28 22"><path d="M0 0h8l7 11-7 11H0l7-11z M12 0h8l7 11-7 11h-8l7-11z" fill="#1aa3d6"/></svg>CFO Consulting Services</h3>
      <p>Senior financial leadership without the cost of a full-time hire.</p>
      <ul>
        <li>Part-time CFO leadership</li>
        <li>Board and lender reporting</li>
        <li>Budgets and cash forecasts</li>
        <li>Process and controls review</li>
      </ul>
    </div>
  </div>
</section>

<section class="sheet sheet-outside" aria-label="Brochure cover panel">
  <div class="frame-rule rule-left"></div>
  <div class="brand">
    <span class="brand-mark"></span>
    <span class="brand-name">Brightfen Partners</span>
  </div>
  <div class="headline-bar"></div>
  <h1 class="headline">
    <span class="line big">We are unique</span>
    <span class="line small">in our abilities</span>
    <span class="line small">and experience</span>
  </h1>
  <div class="photo photo-executive" role="img" aria-label="Photo of a businessman standing at a window overlooking industrial tanks"></div>
  <div class="frame-rule rule-bottom"></div>
</section>

</body>
</html>
```